Stationery Design Project

I have recently had developed a logo for my new company Northbay Venture Partners -see logo attached.
I now need the following
1. Letterhead design as Word template
text needs to show the logo and then
Northbay Venture Partners Pty Ltd
ABN 83 402 615 938
Level 5, Arbour House
17 Pellmont Place
Baulkham Hills, NSW 2153
Tel: + 61(0)2 9374 2816
www.northbayventurepartners.com
lucasd@northbayventurepartners.com
2. Business card -print ready -
Front side needs to show logo then text as follows
Lucas Drayton
CEO
Level 5, Arbour House
17 Pellmont Place
Baulkham Hills, NSW 2153
T: + 61 (0)2 9374 2816
M: + 61 (0)438 721 604
lucasd@pelvarogroup.com.au
On the back of the business card should appear the logo then text as follows
Correct text for the back of the card now in the attached word file please use bold and italics as indicated. Thanks
3. With compliments slip: Including logo + the web address www.northbayventurepartners.com
With compliments slip should fit 3 to an A4 sheet
4. Envelop design including logo + address
For the ethos of the company original brief for the logo below:
I am creating a new business advisory company called Northbay Venture Partners. the Web address will be www.northbayventurepartners.com This business is focused on assisting medium size businesses to achieve their growth objectives. The three pillars are self explanatory -it is focused on businesses that seek to build a global footprint, they seek to define/refine their business model and strategy, they are forward looking and focused on achieving growth.
The ethos of this company will be innovative thinking, passionate, dynamic, entrepreneurial this should reflected in the logo. That said the Logo should not be 'complicated' it should be simple and elegant...
Thanks Lucas Drayton
Reason: I have been travelling all this week -so will only get a chance to review this weekend. Thanks
Target Market(s)
Medium sized business owners with sales between US$5m and $50m.
Industry/Entity Type
Business
Look and feel

```html
<!DOCTYPE html>
<html lang="en">
<head>
<meta charset="utf-8">
<title>Northbay Venture Partners — Business Card</title>
<link rel="stylesheet" href="https://fonts.googleapis.com/css2?family=Open+Sans:wght@400;600;700&display=swap">
<style>
  :root {
    --page-bg: #ece9e4;
    --card-white: #ffffff;
    --card-white-shade: #f1f1f1;
    --brand-blue: #0a8ccf;
    --brand-blue-deep: #0a4f9e;
    --brand-blue-mid: #0b6fb8;
    --text-grey: #6b6b6b;
    --text-dark: #4a4a4a;
    --rule-grey: #c9c9c9;
  }
  html, body {
    margin: 0;
    padding: 0;
    width: 1200px;
    height: 1023px;
    overflow: hidden;
    background: var(--page-bg);
    font-family: "Open Sans", Arial, sans-serif;
  }
  .stationery {
    width: 1200px;
    height: 1023px;
    display: flex;
    align-items: center;
    justify-content: center;
    gap: 40px;
  }
  .card {
    width: 540px;
    height: 330px;
    border-radius: 4px;
    box-shadow: 0 10px 28px rgba(0, 0, 0, 0.18);
    position: relative;
    overflow: hidden;
    box-sizing: border-box;
  }
  .card--front {
    background: linear-gradient(135deg, var(--card-white) 0%, var(--card-white-shade) 100%);
    padding: 36px 44px;
    display: flex;
    flex-direction: column;
    justify-content: space-between;
  }
  .card--back {
    background: linear-gradient(160deg, var(--brand-blue) 0%, var(--brand-blue-mid) 45%, var(--brand-blue-deep) 100%);
  }
  .brand-lockup {
    display: flex;
    align-items: center;
    gap: 20px;
  }
  .brand-dot {
    width: 48px;
    height: 48px;
    border-radius: 50%;
    background: var(--brand-blue);
    flex: none;
  }
  .brand-rule {
    width: 1px;
    height: 84px;
    background: var(--rule-grey);
    flex: none;
  }
  .brand-name {
    margin: 0;
    font-weight: 600;
    font-size: 24px;
    line-height: 1.15;
    color: var(--text-grey);
  }
  .brand-name span {
    display: block;
  }
  .contact {
    font-size: 11.5px;
    line-height: 1.45;
    color: var(--text-grey);
  }
  .contact__name {
    margin: 0;
    font-size: 17px;
    font-weight: 700;
    line-height: 1.2;
    color: var(--text-dark);
  }
  .contact__title {
    margin: 0 0 8px;
    font-size: 12px;
    font-weight: 600;
    color: var(--brand-blue);
  }
  .contact__lines {
    margin: 0;
    font-style: normal;
  }
  .contact__lines span {
    display: block;
  }
</style>
</head>
<body>
  <main class="stationery">
    <section class="card card--front" aria-label="Business card front">
      <div class="brand-lockup">
        <div class="brand-dot"></div>
        <div class="brand-rule"></div>
        <h1 class="brand-name">
          <span>Northbay</span>
          <span>Venture</span>
          <span>Partners</span>
        </h1>
      </div>
      <div class="contact">
        <p class="contact__name">Lucas Drayton</p>
        <p class="contact__title">CEO</p>
        <address class="contact__lines">
          <span>Level 5, Arbour House</span>
          <span>17 Pellmont Place</span>
          <span>Baulkham Hills, NSW 2153</span>
          <span>T: + 61 (0)2 9374 2816</span>
          <span>M: + 61 (0)438 721 604</span>
          <span>lucasd@pelvarogroup.com.au</span>
        </address>
      </div>
    </section>
    <section class="card card--back" aria-label="Business card back"></section>
  </main>
</body>
</html>
```